Postcard Design for Guaranteed Student Leads Campaign

Dimensions: 6" high, 9" wide (Full Bleed: 6.22"x9.21")

I attached a postcard design that I don't like. The postcard design needs to resonate with someone who loves everything about running a massage therapy school. Within a split second, without reading anything on the postcard, it has to visually resonate with someone who spends a lot of time teaching massage therapy.

All of the information needed is on the postcard design I uploaded, please use all the information that is on the postcard (don't leave anything off), but please use different pictures and graphics.

The web address and qr code on the postcard lead to this landing page www.PupilFlowAssured.net/Bodywork

Please take a look at the landing page for theme and color ideas, the picture on the landing page is just a placeholder and will be changed as well. The design of the postcard should match fairly well with the landing page.

Target Market(s)

Massage schools

Industry/Entity Type

trade schools

Requirements
Must have
• beautiful design that resonates with the audience and matches landing page
Nice to have
• I do not like the design of the postcard I uploaded, but all the information on it is correct. We need final vector files so we can make final adjustments.

```html
<!DOCTYPE html>
<html lang="en">
<head>
<meta charset="utf-8">
<title>Pupil Intake Engine – Massage School Postcard</title>
<link href="https://fonts.googleapis.com/css2?family=Poppins:wght@400;500;600;700;800&display=swap" rel="stylesheet">
<style>
  :root {
    --backdrop: #ecebea;
    --card: #ffffff;
    --teal: #5fc4be;
    --teal-deep: #3aa7a1;
    --teal-pale: #e6f6f5;
    --sky: #4fb0d6;
    --charcoal: #2a3235;
    --ink: #1e2224;
    --white: #ffffff;
  }
  * { box-sizing: border-box; margin: 0; padding: 0; }
  html, body { width: 1200px; height: 1200px; overflow: hidden; }
  body {
    background: var(--backdrop);
    font-family: "Poppins", sans-serif;
    color: var(--ink);
    position: relative;
  }
  .postcard {
    position: absolute;
    left: 50px; top: 228px;
    width: 1100px; height: 743px;
    background: var(--card);
    overflow: hidden;
  }
  .therapy-photo {
    position: absolute; inset: 0;
    width: 1100px; height: 743px;
  }
  .content {
    position: absolute; left: 60px; top: 48px;
    width: 590px;
  }
  .brand {
    display: flex; align-items: center; gap: 12px;
    font-weight: 600; font-size: 30px; color: var(--charcoal);
    line-height: 40px;
  }
  .brand-square { width: 26px; height: 26px; background: var(--teal); }
  .audience-tag {
    display: inline-block; margin-top: 30px;
    background: var(--charcoal); color: var(--white);
    font-size: 22px; font-weight: 400;
    padding: 0 22px; line-height: 42px;
  }
  .headline {
    margin-top: 14px;
    color: var(--teal); font-weight: 800; line-height: 1;
  }
  .headline-big { display: block; font-size: 96px; letter-spacing: -1px; }
  .headline-rest { display: block; font-size: 56px; margin-top: 2px; color: var(--teal-deep); }
  .subline {
    margin-top: 16px;
    font-size: 17px; font-weight: 500;
  }
  .benefits {
    margin-top: 14px; list-style: none;
  }
  .benefits li {
    position: relative; padding-left: 22px;
    font-size: 15px; line-height: 28px;
  }
  .benefits li::before {
    content: ""; position: absolute; left: 2px; top: 10px;
    width: 8px; height: 8px; background: var(--teal);
    transform: rotate(45deg);
  }
  .cta {
    position: relative; margin-top: 20px;
    width: 590px; height: 122px;
    background: var(--charcoal);
    border-left: 10px solid var(--teal);
    display: flex; align-items: center;
    padding: 0 13px 0 22px; gap: 16px;
  }
  .cta-text { flex: 1; color: var(--white); }
  .cta-title { font-size: 19px; font-weight: 700; line-height: 28px; }
  .cta-sub { font-size: 15px; font-weight: 400; line-height: 23px; }
  .qr-slot {
    width: 96px; height: 96px; flex: none;
    background: var(--white);
    border: 3px dashed var(--teal);
  }
  .contact {
    margin-top: 18px;
    font-size: 16px; line-height: 27px;
  }
  .contact-row { display: flex; align-items: center; gap: 9px; }
  .contact-row svg { width: 15px; height: 15px; }
</style>
</head>
<body>
  <section class="postcard">
    <svg class="therapy-photo" viewBox="0 0 1100 743">
      <defs>
        <linearGradient id="photoTone" x1="0" y1="0" x2="0.5" y2="1">
          <stop offset="0" stop-color="var(--sky)"/>
          <stop offset="0.5" stop-color="#86cdd6"/>
          <stop offset="1" stop-color="#b9e3df"/>
        </linearGradient>
      </defs>
      <path d="M740,0 C660,180 660,560 760,743 L724,743 C620,560 620,180 704,0 Z" fill="var(--teal-pale)"/>
      <path d="M760,0 C680,180 680,560 780,743 L1100,743 L1100,0 Z" fill="url(#photoTone)" role="img" aria-label="Photo of a massage instructor guiding a student's hands on a client's shoulder in a bright treatment room"/>
    </svg>

    <div class="content">
      <div class="brand"><span class="brand-square"></span>PupilFlow</div>

      <div class="audience-tag">Massage School Student</div>

      <h1 class="headline">
        <span class="headline-big">10 FREE</span>
        <span class="headline-rest">STUDENT LEADS</span>
      </h1>
      <p class="subline">For a limited time, try the Pupil Intake Engine, risk-free.</p>

      <ul class="benefits">
        <li>Massage School students looking for a massage schools in your area</li>
        <li>Exclusive Leads (not shared with other schools)</li>
        <li>10 Guaranteed Free Leads</li>
        <li>Simple Setup Precess (Less than 5minutes)</li>
      </ul>

      <div class="cta">
        <div class="cta-text">
          <p class="cta-title">GET YOUR 10 FREE STUDENT LEADS NOW</p>
          <p class="cta-sub">Scan the QR code to start getting your 10 free leads</p>
          <p class="cta-sub">(takes less than 5 minutes)</p>
        </div>
        <div class="qr-slot" role="img" aria-label="QR code linking to the landing page"></div>
      </div>

      <div class="contact">
        <div class="contact-row">
          <svg viewBox="0 0 24 24"><path fill="var(--ink)" d="M6.6 10.8a15.1 15.1 0 0 0 6.6 6.6l2.2-2.2a1 1 0 0 1 1-.25 11.4 11.4 0 0 0 3.6.57 1 1 0 0 1 1 1V20a1 1 0 0 1-1 1A17 17 0 0 1 3 4a1 1 0 0 1 1-1h3.5a1 1 0 0 1 1 1c0 1.25.2 2.45.57 3.6a1 1 0 0 1-.25 1z"/></svg>
          <span>(555) 014-2290</span>
        </div>
        <div class="contact-row">
          <svg viewBox="0 0 24 24"><circle cx="12" cy="12" r="9" fill="none" stroke="var(--ink)" stroke-width="2.4"/><path d="M3 12h18M12 3c3 3.5 3 14.5 0 18M12 3c-3 3.5-3 14.5 0 18" fill="none" stroke="var(--ink)" stroke-width="2"/></svg>
          <span>www.PupilFlowAssured.net/Bodywork/</span>
        </div>
      </div>
    </div>
  </section>
</body>
</html>
```